Fernly Garage Doors Business Card

I need a Business Card for my garage door business:
Fernly Garage Doors.
please add:
logo
phone number: 833-2-FERNLY
(337-659)

email: service@fernlygaragedoors.com
website: www.fernlygaragedoors.com

The attached image is recommendation ONLY.

```html
<!DOCTYPE html>
<html lang="en">
<head>
<meta charset="utf-8">
<title>Fernly Garage Doors – Business Card</title>
<link rel="stylesheet" href="https://fonts.googleapis.com/css2?family=Comfortaa:wght@600&family=Oswald:wght@300;400&display=swap">
<style>
  :root {
    --mint: #bfe5da;
    --card-black: #231f20;
    --teal: #52c5d0;
    --white: #ffffff;
  }
  * { margin: 0; padding: 0; box-sizing: border-box; }
  html, body { width: 1200px; height: 856px; overflow: hidden; }
  body {
    background: var(--mint);
    position: relative;
    font-family: "Oswald", sans-serif;
  }
  .card {
    position: absolute;
    width: 620px;
    height: 354px;
    background: var(--card-black);
    border-radius: 30px;
    overflow: hidden;
    box-shadow: 0 10px 26px rgba(40, 90, 80, 0.25);
  }
  /* Front */
  .card--front { left: 130px; top: 60px; }
  .front-brand {
    position: absolute;
    inset: 0;
    display: flex;
    flex-direction: column;
    align-items: center;
    justify-content: center;
    gap: 28px;
  }
  .brand-square {
    width: 92px;
    height: 92px;
    background: var(--teal);
    border-radius: 6px;
  }
  .brand-name {
    font-family: "Comfortaa", sans-serif;
    font-weight: 600;
    color: var(--white);
    line-height: 1.05;
  }
  .card--front .brand-name { font-size: 40px; text-align: left; }
  .brand-name span { display: block; }
  .brand-name .line-2 { padding-left: 30px; }

  /* Back */
  .card--back { left: 450px; top: 442px; }
  .accent-panel {
    position: absolute;
    left: 0; top: 0; bottom: 0;
    width: 210px;
    background: linear-gradient(180deg, #5ccad4, #45b8c6);
  }
  .back-content {
    position: absolute;
    left: 250px;
    top: 40px;
    right: 24px;
  }
  .card--back .brand-name { font-size: 32px; margin-bottom: 22px; }
  .card--back .brand-name .line-2 { padding-left: 22px; }
  .contact-list { list-style: none; }
  .contact-item {
    display: flex;
    align-items: center;
    gap: 14px;
    color: var(--white);
    font-weight: 300;
    font-size: 21px;
    letter-spacing: 0.2px;
    margin-bottom: 14px;
  }
  .contact-icon {
    flex: none;
    width: 38px;
    height: 38px;
    border-radius: 50%;
    background: var(--teal);
    display: flex;
    align-items: center;
    justify-content: center;
  }
  .contact-icon svg { width: 20px; height: 20px; }
</style>
</head>
<body>

  <section class="card card--front" aria-label="Business card front">
    <div class="front-brand">
      <div class="brand-square"></div>
      <h1 class="brand-name"><span>Fernly</span><span class="line-2">Garage Doors</span></h1>
    </div>
  </section>

  <section class="card card--back" aria-label="Business card back">
    <div class="accent-panel"></div>
    <div class="back-content">
      <h2 class="brand-name"><span>Fernly</span><span class="line-2">Garage Doors</span></h2>
      <ul class="contact-list">
        <li class="contact-item">
          <span class="contact-icon">
            <svg viewBox="0 0 24 24"><path fill="#231f20" d="M6.6 10.8a15.1 15.1 0 0 0 6.6 6.6l2.2-2.2c.3-.3.7-.4 1-.2 1.1.4 2.3.6 3.6.6.6 0 1 .4 1 1V20c0 .6-.4 1-1 1A17 17 0 0 1 3 4c0-.6.4-1 1-1h3.5c.6 0 1 .4 1 1 0 1.3.2 2.5.6 3.6.1.3 0 .7-.2 1z"/></svg>
          </span>
          833-2-FERNLY (337-659)
        </li>
        <li class="contact-item">
          <span class="contact-icon">
            <svg viewBox="0 0 24 24"><rect x="3" y="6" width="18" height="12" fill="#231f20"/><path d="M3 6l9 7 9-7M3 18l7-6M21 18l-7-6" stroke="#52c5d0" stroke-width="1.4" fill="none"/></svg>
          </span>
          service@fernlygaragedoors.com
        </li>
        <li class="contact-item">
          <span class="contact-icon">
            <svg viewBox="0 0 24 24" fill="none" stroke="#231f20" stroke-width="1.8"><circle cx="12" cy="12" r="9"/><ellipse cx="12" cy="12" rx="4" ry="9"/><path d="M3 12h18M5 7h14M5 17h14"/></svg>
          </span>
          www.fernlygaragedoors.com
        </li>
      </ul>
    </div>
  </section>

</body>
</html>
```